Boutique Recruiting Firm Needs Eye-Catching Business Cards (and potentially new logo)!

I run a recruiting company in Charleston, South Carolina. I have a ton of networking events coming up and need business cards to grab potential clients attention.

I currently have a logo but if you want to try and recreate the logo to something more modern I am open to that. If you do decide to create a new logo please submit the business card with the old logo and the new one.

Staffing Under Blue Lanterns, LLC is the name of my company. I create videos to my clients and candidates which allows me to standout from my competition so I would like a business card (and possibly new logo) to do the same.

I do not specialize in any one industry of recruiting.

```html
<!DOCTYPE html>
<html lang="en">
<head>
<meta charset="utf-8">
<title>Staffing Under Blue Lanterns — Business Cards</title>
<link href="https://fonts.googleapis.com/css2?family=Open+Sans:wght@400;700&display=swap" rel="stylesheet">
<style>
  :root {
    --backdrop: #4a423e;
    --card: #0d0d0d;
    --ink: #f2f2f2;
    --ink-soft: #cfcfcf;
    --rule: #8a8a8a;
  }
  * { box-sizing: border-box; margin: 0; padding: 0; }
  html, body { width: 1200px; height: 814px; overflow: hidden; }
  body {
    background: var(--backdrop);
    font-family: "Open Sans", Arial, sans-serif;
    color: var(--ink);
    position: relative;
  }
  .card {
    position: absolute;
    width: 520px;
    height: 298px;
    background: var(--card);
    border-radius: 4px;
    box-shadow: 0 10px 24px rgba(0,0,0,.35);
  }
  .card--front { left: 55px; top: 258px; }
  .card--back  { left: 625px; top: 258px; }

  .brand {
    display: flex;
    align-items: center;
    gap: 10px;
    font-weight: 700;
    color: var(--ink);
    line-height: 1.05;
  }
  .brand__mark {
    width: 14px; height: 14px;
    background: var(--ink);
    flex: none;
  }
  .card--front .brand { position: absolute; left: 70px; top: 48px; font-size: 24px; }
  .card--back .brand { position: absolute; left: 0; right: 0; top: 108px; justify-content: center; font-size: 24px; }

  .contact {
    position: absolute;
    left: 0; right: 0; top: 148px;
    display: flex;
    justify-content: center;
  }
  .contact__person {
    text-align: right;
    padding-right: 18px;
    font-size: 13.5px;
    line-height: 1.55;
    color: var(--ink-soft);
  }
  .contact__name { font-size: 16px; font-weight: 700; color: var(--ink); }
  .contact__rule { width: 1px; background: var(--rule); margin-top: 2px; height: 100px; }
  .contact__lines {
    list-style: none;
    padding-left: 16px;
    font-size: 12.5px;
    line-height: 1.65;
    color: var(--ink-soft);
  }
  .contact__lines li { display: flex; align-items: center; gap: 9px; }
  .contact__lines svg { width: 12px; height: 12px; fill: var(--ink); flex: none; }

  .web {
    position: absolute;
    left: 0; right: 0; top: 178px;
    text-align: center;
    font-size: 11px;
    letter-spacing: 2.5px;
    color: var(--ink-soft);
  }
</style>
</head>
<body>
  <section class="card card--front" aria-label="Business card front">
    <div class="brand"><span class="brand__mark"></span><span>Staffing Under<br>Blue Lanterns, LLC</span></div>
    <div class="contact">
      <div class="contact__person">
        <div class="contact__name">Mara Ellison</div>
        <div>CEO/Founder</div>
        <div>214 Harbor Row</div>
        <div>Charleston, SC 29401</div>
      </div>
      <div class="contact__rule"></div>
      <ul class="contact__lines">
        <li><svg viewBox="0 0 12 12"><path d="M3 1l2 2.5-1.2 1.2a6 6 0 0 0 3.5 3.5L8.5 7 11 9l-1.5 2C5 11 1 7 1 2.5z"/></svg>555 210 4471</li>
        <li><svg viewBox="0 0 12 12"><path d="M3 0h6v12H3zM4 1.5v7.5h4V1.5z"/></svg>555 388 1026</li>
        <li><svg viewBox="0 0 12 12"><path d="M3 1h6v3H3zM1 5h10v5H9v2H3v-2H1zM4 8v3h4V8z"/></svg>555 907 5532</li>
        <li><svg viewBox="0 0 12 12"><path d="M0 2h12v8H0zM1 3l5 3.5L11 3z" fill-rule="evenodd"/></svg>hello@bluelanterns.co</li>
      </ul>
    </div>
  </section>

  <section class="card card--back" aria-label="Business card back">
    <div class="brand"><span class="brand__mark"></span><span>Staffing Under<br>Blue Lanterns, LLC</span></div>
    <div class="web">www.bluelanterns.co</div>
  </section>
</body>
</html>
```